Social Media Monitoring Web Site Design

We need a responsive web design for a new company based in Ireland. We offer a social media monitoring service that works in a call centre environment. Our service name is 'VANTO'. We have a logo that is attached.

Sites we like (in no particular order):

1. http://www.plumvector.com/
2. https://taldrix.io/
3. https://www.loomhaven.com/

We want the web site to have the following sections:

HOME
VANTO PLATFORM
VANTO SERVICE
CASE STUDIES
ABOUT US
CONTACT US

We also need a customer Login link. The site must be a responsive design.

Target Market(s)

Corporate Customers

Industry/Entity Type

It Company

Coding

Coded - Design and coding required

Number of Pages Required

2 page

Requirements
Must have
• Responsive Design
• Bootstrap
Nice to have
• Animations

```html
<!DOCTYPE html>
<html lang="en">
<head>
<meta charset="utf-8">
<title>VANTO – Social Media Monitoring</title>
<link href="https://fonts.googleapis.com/css2?family=Montserrat:wght@400;500;600;700&display=swap" rel="stylesheet">
<style>
:root{
  --white:#ffffff;
  --ink:#3d3d3d;
  --body-text:#8a8a8a;
  --orange:#e0762f;
  --blue:#3d9be0;
  --field:#f1f1f1;
  --field-line:#dcdcdc;
  --footer:#1f1f1f;
  --footer-base:#161616;
  --footer-text:#b5b5b5;
}
*{margin:0;padding:0;box-sizing:border-box}
html,body{width:1200px;height:3130px;overflow:hidden}
body{font-family:'Montserrat',sans-serif;color:var(--ink);background:var(--white);position:relative}
section,footer{position:absolute;left:0;width:1200px}
.abs{position:absolute}

/* hero */
.hero{top:0;height:555px;overflow:hidden}
.hero-photo{position:absolute;inset:0;background:radial-gradient(ellipse at 60% 40%,#d7b79a 0%,#b38d6d 40%,#7b5a44 100%)}
.hero-shade{position:absolute;inset:0;background:rgba(40,25,15,.25)}
.brand{left:100px;top:32px;display:flex;align-items:center;gap:12px;color:var(--white)}
.brand-mark{width:42px;height:42px;background:var(--orange)}
.brand-name{font-size:40px;font-weight:600;letter-spacing:2px;line-height:1}
.nav{left:405px;top:60px;display:flex;gap:26px;list-style:none}
.nav li{font-size:13px;font-weight:500;color:var(--white)}
.hero-title{top:195px;width:1200px;text-align:center;color:var(--white);font-size:60px;font-weight:700;letter-spacing:1px}
.hero-sub{top:283px;width:1200px;text-align:center;color:var(--white);font-size:30px;font-weight:400}
.btn-start{left:459px;top:359px;width:282px;height:75px;background:var(--orange);color:var(--white);font-size:24px;font-weight:700;display:flex;align-items:center;justify-content:center}
.dots{left:569px;top:503px;display:flex;gap:14px}
.dots span{width:11px;height:11px;border-radius:50%;background:var(--white)}
.dots span.on{background:var(--orange)}

/* platform */
.platform{top:555px;height:488px}
.platform-phone{left:108px;top:75px;width:274px;height:413px;border-radius:34px 34px 0 0;background:linear-gradient(160deg,#2c2c2c,#111);padding:40px 20px 0}
.platform-phone div{width:100%;height:100%;background:linear-gradient(135deg,#8b5a36,#5a3a25 55%,#c9b8a3)}
.section-title{font-size:38px;font-weight:500;color:var(--ink);letter-spacing:.5px}
.platform .section-title{left:407px;top:62px}
.platform-copy{left:407px;top:130px;width:695px}
.platform-copy p{font-size:12px;line-height:21px;color:var(--body-text);margin-bottom:21px}
.btn-blue{background:var(--blue);color:var(--white);font-size:15px;font-weight:600;display:flex;align-items:center;justify-content:center}
.platform .btn-blue{left:407px;top:367px;width:173px;height:61px}

/* services */
.services{top:1043px;height:474px;overflow:hidden;color:var(--white)}
.services-photo{position:absolute;inset:0;background:linear-gradient(100deg,#6d5446 0%,#8a6a55 45%,#5e4a40 100%)}
.services .section-title{top:48px;width:1200px;text-align:center;color:var(--white)}
.service{top:141px;width:340px;text-align:center}
.service-icon{width:124px;height:124px;border:4px solid var(--white);border-radius:50%;margin:0 auto;display:flex;align-items:center;justify-content:center}
.service h3{margin-top:38px;font-size:25px;font-weight:500}
.service p{margin-top:10px;font-size:12px;font-weight:600;line-height:21px;padding:0 18px}
.slide-arrow{top:207px}

/* case studies */
.cases{top:1517px;height:378px}
.cases .section-title{top:52px;width:1200px;text-align:center}
.case-tile{top:148px;width:240px;height:144px;color:var(--white);font-size:24px;font-weight:600;display:flex;align-items:center;justify-content:center;letter-spacing:1px}
.case-tile.blue{background:var(--blue)}
.case-tile.orange{background:var(--orange)}

/* about */
.about{top:1895px;height:326px;overflow:hidden;color:var(--white)}
.about-photo{position:absolute;inset:0;background:linear-gradient(100deg,#5a4538 0%,#7a6050 50%,#4a3a30 100%)}
.about .section-title{top:60px;width:1200px;text-align:center;color:var(--white)}
.about-copy{top:130px;left:160px;width:880px;text-align:center;font-size:13px;font-weight:500;line-height:23px}
.btn-outline{left:520px;top:207px;width:158px;height:62px;border:1px solid var(--white);font-size:14px;font-weight:500;display:flex;align-items:center;justify-content:center}

/* contact */
.contact{top:2221px;height:540px}
.contact .section-title{top:50px;width:1200px;text-align:center}
.field{background:var(--field);border:1px solid var(--field-line);font-size:12px;font-weight:500;color:var(--ink);padding:22px 18px}
.contact .btn-blue{left:273px;top:436px;width:113px;height:60px;font-size:14px}

/* footer */
.site-footer{top:2761px;height:369px;background:var(--footer);color:var(--white)}
.footer-col{top:44px}
.footer-col h4{font-size:20px;font-weight:500;margin-bottom:18px}
.footer-col ul{list-style:none}
.footer-col li{font-size:12px;color:var(--footer-text);line-height:21px}
.social li{display:flex;align-items:center;gap:16px;margin-bottom:8px}
.social li span{width:34px;height:34px;border:1px solid #555}
.footer-base{left:0;top:286px;width:1200px;height:83px;background:var(--footer-base);font-size:12px;color:var(--footer-text);display:flex;align-items:center;justify-content:center}
</style>
</head>
<body>

<section class="hero">
  <div class="hero-photo" role="img" aria-label="Blurred photo of a woman taking a selfie with a smartphone"></div>
  <div class="hero-shade"></div>
  <div class="brand abs">
    <div class="brand-mark"></div>
    <div class="brand-name">VANTO</div>
  </div>
  <ul class="nav abs">
    <li>HOME</li><li>VANTO PLATFORM</li><li>VANTO SERVICES</li><li>CASE STUDIES</li><li>ABOUT US</li><li>CONTACT US</li>
  </ul>
  <h1 class="hero-title abs">SOCIAL MEDIA MONITORING</h1>
  <p class="hero-sub abs">Works in a Call Centre Environment</p>
  <div class="btn-start abs">GET STARTED</div>
  <div class="dots abs"><span></span><span class="on"></span><span></span></div>
</section>

<section class="platform">
  <div class="platform-phone abs"><div role="img" aria-label="Smartphone showing a tablet with wooden letter blocks spelling social media words"></div></div>
  <h2 class="section-title abs">VANTO PLATFORM</h2>
  <div class="platform-copy abs">
    <p>Our platform gathers public posts, mentions and replies from every major network and routes them straight to your agents. Each item is scored for urgency, tagged by topic and placed in a shared queue so that nothing is missed and every customer gets a timely answer, whatever the hour or channel, and teams can see at a glance what needs doing next.</p>
    <p>Supervisors see live volumes, response times and sentiment on one screen, while agents work from the same desktop they already use. Rules can be set to escalate a complaint, flag a journalist or hold a reply for approval, and every action is logged for reporting and training across the whole team. Reports can be exported each week, shared with managers and compared across brands, regions and campaigns to show clear progress over time.</p>
  </div>
  <div class="btn-blue abs">READ MORE</div>
</section>

<section class="services">
  <div class="services-photo" role="img" aria-label="Blurred photo of a woman wearing headphones"></div>
  <h2 class="section-title abs">VANTO SERVICES</h2>

  <svg class="abs slide-arrow" style="left:30px" width="34" height="52" viewBox="0 0 34 52"><path d="M28 4 L8 26 L28 48" fill="none" stroke="#ffffff" stroke-opacity=".6" stroke-width="7"/></svg>
  <svg class="abs slide-arrow" style="left:1130px" width="34" height="52" viewBox="0 0 34 52"><path d="M6 4 L26 26 L6 48" fill="none" stroke="#ffffff" stroke-opacity=".6" stroke-width="7"/></svg>

  <div class="service abs" style="left:70px">
    <div class="service-icon">
      <svg width="70" height="56" viewBox="0 0 70 56" fill="#ffffff"><circle cx="35" cy="14" r="10"/><path d="M18 54 a17 17 0 0 1 34 0z"/><circle cx="13" cy="20" r="7"/><path d="M0 50 a13 13 0 0 1 20 -11 v11z"/><circle cx="57" cy="20" r="7"/><path d="M70 50 a13 13 0 0 0 -20 -11 v11z"/></svg>
    </div>
    <h3>Crisis Prevention</h3>
    <p>Spot rising complaints early and alert the right people before a story spreads online</p>
  </div>
  <div class="service abs" style="left:431px">
    <div class="service-icon">
      <svg width="60" height="52" viewBox="0 0 60 52" fill="#ffffff"><path d="M6 2 h48 a6 6 0 0 1 6 6 v26 a6 6 0 0 1 -6 6 h-30 l-12 12 v-12 h-6 a6 6 0 0 1 -6 -6 v-26 a6 6 0 0 1 6 -6z"/></svg>
    </div>
    <h3>Chatter Monitoring</h3>
    <p>Track mentions, replies and hashtags in real time and answer them from one queue</p>
  </div>
  <div class="service abs" style="left:788px">
    <div class="service-icon">
      <svg width="64" height="60" viewBox="0 0 64 60"><path d="M10 34 v-6 a22 22 0 0 1 44 0 v6" fill="none" stroke="#ffffff" stroke-width="5"/><rect x="4" y="30" width="12" height="20" rx="4" fill="#ffffff"/><rect x="48" y="30" width="12" height="20" rx="4" fill="#ffffff"/><circle cx="32" cy="36" r="12" fill="#ffffff"/><path d="M54 48 q0 8 -14 8" fill="none" stroke="#ffffff" stroke-width="3"/></svg>
    </div>
    <h3>Celebrity</h3>
    <p>Watch talk around public figures and respond quickly when attention suddenly peaks</p>
  </div>
</section>

<section class="cases">
  <h2 class="section-title abs">CASE STUDIES</h2>
  <div class="case-tile blue abs" style="left:98px">Norvell</div>
  <div class="case-tile orange abs" style="left:353px">Quarra</div>
  <div class="case-tile blue abs" style="left:605px">LUMENO</div>
  <div class="case-tile orange abs" style="left:858px">KAVIX</div>
</section>

<section class="about">
  <div class="about-photo" role="img" aria-label="Photo of a man sitting on a wooden deck holding a smartphone"></div>
  <h2 class="section-title abs">ABOUT US</h2>
  <p class="about-copy abs">We are a small team in Ireland building tools that help contact centres listen, respond and learn from every public conversation about their brand.</p>
  <div class="btn-outline abs">READ MORE</div>
</section>

<section class="contact">
  <h2 class="section-title abs">CONTACT US</h2>
  <div class="field abs" style="left:275px;top:141px;width:314px;height:65px">Name</div>
  <div class="field abs" style="left:609px;top:141px;width:313px;height:65px">Email</div>
  <div class="field abs" style="left:275px;top:229px;width:647px;height:175px">Message</div>
  <div class="btn-blue abs">SUBMIT</div>
</section>

<footer class="site-footer">
  <div class="footer-col abs" style="left:98px">
    <h4>ABOUT US</h4>
    <ul><li>Home</li><li>Vanto Platform</li><li>Vanto Services</li><li>Case Studies</li><li>About us</li><li>Contact us</li></ul>
  </div>
  <div class="footer-col abs" style="left:390px">
    <h4>COMPANY</h4>
    <ul><li>About Us</li><li>Careers</li><li>Events</li><li>Contact Us</li><li>The Team</li><li>Press</li><li>Partnerships</li></ul>
  </div>
  <div class="footer-col abs" style="left:689px">
    <h4>PRODUCT</h4>
    <ul><li>About Us</li><li>Careers</li><li>Events</li><li>Contact Us</li><li>The Team</li><li>Press</li><li>Partnerships</li></ul>
  </div>
  <div class="footer-col abs" style="left:950px">
    <h4>GET CONNECT</h4>
    <ul class="social"><li><span></span>Friendlink</li><li><span></span>Chatter</li><li><span></span>Rss</li></ul>
  </div>
  <div class="footer-base abs">© 2015 brevano.co.uk. All rights reserved.</div>
</footer>

</body>
</html>
```